Web Design for company in the healthcare industry

We need a web design for a new company in the healthcare industry (telehealth) which allows patients to schedule appointments at their convenience, view and monitor their results, and consult with specialists that fit their requirements. The aim is to help patients take charge of their own health.

We already have a logo (attached) and are working with a developer who will do all the back end programming once the design is ready. Apart from the colours in the logo, we think shades of gray would work well.

Target Market(s)

I imagine the vast majority would be professionals from 30-50 years old.

Industry/Entity Type

Health And Wellness

Number of Pages Required

4 page

Requirements
Must have
• Hand-sketched graphics, particularly on landing page.
Should not have
• We don't want any photographs of people

```html
<!DOCTYPE html>
<html lang="en">
<head>
<meta charset="utf-8">
<title>Medivara – Telehealth</title>
<link href="https://fonts.googleapis.com/css2?family=Open+Sans:wght@400;600;700&display=swap" rel="stylesheet">
<style>
:root{
  --green:#7bbf3f;
  --green-dark:#5f9e2a;
  --blue:#1f6fb8;
  --blue-dark:#175a99;
  --ink:#3b3f44;
  --muted:#8a9097;
  --line:#e2e5e8;
  --panel:#f0f1f3;
  --white:#ffffff;
}
*{margin:0;padding:0;box-sizing:border-box}
html,body{width:814px;height:1200px;overflow:hidden;background:var(--white)}
body{font-family:"Open Sans",Arial,sans-serif;color:var(--ink);font-size:9px;line-height:1.5}
.page{width:814px;height:1200px;position:relative}

.site-header{height:36px;display:flex;align-items:center;justify-content:space-between;padding:0 34px}
.brand{display:flex;align-items:center;gap:6px;font-size:19px;font-weight:700;color:var(--blue)}
.brand-dot{width:12px;height:12px;border-radius:50%;background:var(--green)}
.main-nav{display:flex;gap:4px}
.main-nav a{font-size:9px;color:var(--ink);text-decoration:none;padding:5px 10px}
.main-nav a.active{background:var(--green);color:var(--white)}

.hero{position:relative;height:264px;overflow:hidden}
.hero-photo{position:absolute;inset:0;background:radial-gradient(ellipse at 50% 40%,#4a6c86 0%,#2a4459 45%,#1a2b3a 100%)}
.steps{position:relative;display:flex;justify-content:space-between;padding:0 70px;margin-top:72px}
.steps-line{position:absolute;left:120px;right:120px;top:30px;height:2px;background:var(--white)}
.step{width:160px;text-align:center;position:relative}
.step-icon{width:62px;height:62px;margin:0 auto;border-radius:50%;background:var(--green);border:3px solid var(--white);display:flex;align-items:center;justify-content:center}
.step-label{margin-top:16px;color:var(--white);font-weight:700;font-size:12px;line-height:1.25}

.welcome{text-align:center;padding:32px 90px 26px}
.section-title{font-size:17px;font-weight:600;color:var(--blue);margin-bottom:12px}
.welcome p{color:var(--muted)}

.what-we-do{background:var(--panel);height:228px;padding:34px 56px;display:flex;gap:40px}
.what-text{flex:1}
.what-text .section-title{margin-bottom:10px}
.what-text p{color:var(--muted);margin-bottom:20px}
.btn{display:inline-block;background:var(--green);color:var(--white);font-size:9px;font-weight:600;padding:7px 18px}
.what-image{width:250px;height:150px;background:linear-gradient(135deg,#0d2a4a,#1d5e95 60%,#0b2038)}

.media-row{display:flex;gap:36px;padding:28px 56px 0;height:350px}
.video-col{flex:1.25}
.video-frame{height:200px;background:linear-gradient(160deg,#6f8794,#2f4b5b);position:relative;display:flex;align-items:center;justify-content:center}
.play{width:44px;height:44px;border-radius:50%;background:rgba(255,255,255,.85);display:flex;align-items:center;justify-content:center}
.news-col{flex:1;border-left:1px solid var(--line);padding-left:24px}
.news-item{display:flex;gap:10px;margin-bottom:14px}
.news-thumb{width:52px;height:44px;flex:none}
.news-date{color:var(--green);font-weight:600;font-size:8px}
.news-text{color:var(--muted);font-size:8px;line-height:1.4}
.read-more{color:var(--blue);font-size:8px}

.testimonials{background:var(--panel);height:126px;padding:20px 56px}
.testimonials .section-title{margin-bottom:8px}
.quotes{display:flex;gap:80px}
.quote{flex:1}
.quote-name{color:var(--green);font-weight:600;font-size:9px}
.quote p{color:var(--muted);font-size:8px;line-height:1.4}

.site-footer{position:absolute;left:0;right:0;bottom:0;height:64px;background:var(--blue);color:var(--white);display:flex;align-items:center;justify-content:space-between;padding:0 34px}
.footer-brand{display:flex;align-items:center;gap:6px;font-size:17px;font-weight:700}
.footer-brand .brand-dot{background:var(--white)}
.footer-copy{font-size:7px;opacity:.85;margin-top:2px}
.social{display:flex;align-items:center;gap:8px;font-size:9px}
.social span.circle{width:20px;height:20px;border-radius:50%;background:var(--white);opacity:.9}
</style>
</head>
<body>
<div class="page">
  <header class="site-header">
    <div class="brand"><span class="brand-dot"></span>Medivara</div>
    <nav class="main-nav">
      <a class="active" href="#">Home</a>
      <a href="#">Health Packages</a>
      <a href="#">Appointments</a>
      <a href="#">Specialists</a>
    </nav>
  </header>

  <section class="hero">
    <div class="hero-photo" role="img" aria-label="Dark blue photo of a doctor's desk with a laptop and stethoscope"></div>
    <div class="steps">
      <div class="steps-line"></div>
      <div class="step">
        <div class="step-icon"><svg width="30" height="30" viewBox="0 0 30 30" fill="none" stroke="#fff" stroke-width="2"><path d="M4 6h4l3 13h13l3-9H10"/><circle cx="13" cy="24" r="2"/><circle cx="22" cy="24" r="2"/></svg></div>
        <div class="step-label">Select<br>a Package</div>
      </div>
      <div class="step">
        <div class="step-icon"><svg width="30" height="30" viewBox="0 0 30 30" fill="none" stroke="#fff" stroke-width="2"><rect x="5" y="7" width="20" height="18"/><path d="M5 12h20M10 4v6M20 4v6M9 16h3M14 16h3M19 16h3M9 20h3M14 20h3"/></svg></div>
        <div class="step-label">Schedule An Appointment<br>At Your Convenience</div>
      </div>
      <div class="step">
        <div class="step-icon"><svg width="30" height="30" viewBox="0 0 30 30" fill="none" stroke="#fff" stroke-width="2"><path d="M8 4h10l5 5v17H8z"/><path d="M11 13h9M11 17h9M11 21h6"/></svg></div>
        <div class="step-label">Get Your<br>Result Back</div>
      </div>
      <div class="step">
        <div class="step-icon"><svg width="30" height="30" viewBox="0 0 30 30" fill="none" stroke="#fff" stroke-width="2"><path d="M15 25C6 18 4 14 4 10.5A5.5 5.5 0 0 1 15 8a5.5 5.5 0 0 1 11 2.5C26 14 24 18 15 25z"/></svg></div>
        <div class="step-label">A<br>Healthier You</div>
      </div>
    </div>
  </section>

  <section class="welcome">
    <h1 class="section-title">Welcome to Medivara</h1>
    <p>Our platform lets you book visits when it suits you, follow your test results online and speak with trusted specialists who match your needs. We built every step around your schedule so that caring for your health feels simple, clear and personal. Create your account today and take charge of your own wellbeing with confidence.</p>
  </section>

  <section class="what-we-do">
    <div class="what-text">
      <h2 class="section-title">What We Do</h2>
      <p>We connect patients with qualified doctors through secure video consultations, online appointment booking and a personal results dashboard. Choose a health package, pick a time that works for you and receive clear reports you can share with your family doctor whenever you need.</p>
      <a class="btn" href="#">Learn More</a>
    </div>
    <div class="what-image" role="img" aria-label="Close-up of a blue medical heart monitor display"></div>
  </section>

  <section class="media-row">
    <div class="video-col">
      <h2 class="section-title">Watch How it Works</h2>
      <div class="video-frame" role="img" aria-label="Video still of a clinic room with monitoring equipment">
        <div class="play"><svg width="16" height="16" viewBox="0 0 16 16"><path d="M4 2l10 6-10 6z" fill="#1f6fb8"/></svg></div>
      </div>
    </div>
    <div class="news-col">
      <h2 class="section-title">Latest News</h2>
      <div class="news-item">
        <div class="news-thumb" role="img" aria-label="Thumbnail of medical equipment" style="background:linear-gradient(135deg,#9fb3c2,#4c6a80)"></div>
        <div><div class="news-date">May 06, 2015</div><div class="news-text">New screening packages now available for busy professionals this season.</div><a class="read-more" href="#">Read More »</a></div>
      </div>
      <div class="news-item">
        <div class="news-thumb" role="img" aria-label="Thumbnail of a laboratory sample" style="background:linear-gradient(135deg,#c5cdd4,#7c8d99)"></div>
        <div><div class="news-date">May 04, 2015</div><div class="news-text">Online results dashboard now shows clear trends across all your tests.</div><a class="read-more" href="#">Read More »</a></div>
      </div>
      <div class="news-item">
        <div class="news-thumb" role="img" aria-label="Thumbnail of a stethoscope on a desk" style="background:linear-gradient(135deg,#b8c7d1,#5d7587)"></div>
        <div><div class="news-date">May 01, 2015</div><div class="news-text">More specialists have joined our network to offer evening video consultations.</div><a class="read-more" href="#">Read More »</a></div>
      </div>
    </div>
  </section>

  <section class="testimonials">
    <h2 class="section-title">Testimonials</h2>
    <div class="quotes">
      <div class="quote">
        <div class="quote-name">Sarah Lund</div>
        <p>Booking a consultation took minutes and my results were ready the next day. The specialists explained everything clearly and kindly.</p>
        <a class="read-more" href="#">Read More »</a>
      </div>
      <div class="quote">
        <div class="quote-name">Mark Ellis</div>
        <p>I no longer wait weeks for an appointment. Everything from scheduling to follow-up happens online at a time that suits me.</p>
        <a class="read-more" href="#">Read More »</a>
      </div>
    </div>
  </section>

  <footer class="site-footer">
    <div>
      <div class="footer-brand"><span class="brand-dot"></span>Medivara</div>
      <div class="footer-copy">Copyright © 2015 All Rights Reserved | Privacy Policy</div>
    </div>
    <div class="social">Follow Us:<span class="circle"></span><span class="circle"></span><span class="circle"></span><span class="circle"></span></div>
  </footer>
</div>
</body>
</html>
```